11th Annual Vemtora Forum Flyer - Save the Date

We need a flyer for our annual Forum that will be creative with the theme of the Forum while highlighting our conference Title and Topics. Flyer should allow for a header that can be used consistently across conference communication. This is our 11th Annual Forum, which will take place outside of Houston, Texas at Bel Costano Resort and Spa.

Target Market(s)

Architects, engineers, contractors, universities, building project Owners

Industry/Entity Type

Construction

Font styles to use
Sans Serif

Colors

Designer to choose colors to be used in the design.

Requirements
Must have
• Title, date, location, key topics (title only), logo. See attached for breakdown of information.
Nice to have
• Creativity with the theme of the Forum, ability to slice flyer so that a portion can be used for a header in other conference documents.
• Mention of Closing Keynote, Dale Hutton
Should not have
• Please don't use the topic descriptions in the Flyer. Just the main titles of the topics is necessary.
• Should not be too word, but eye-catching with graphics and main

```html
<!DOCTYPE html>
<html lang="en">
<head>
<meta charset="utf-8">
<title>2019 Vemtora Forum Flyer</title>
<link href="https://fonts.googleapis.com/css2?family=Roboto+Condensed:wght@700&family=Roboto:wght@500&family=Open+Sans:wght@400;700&display=swap" rel="stylesheet">
<style>
  :root{
    --navy:#1b2f6e;
    --blue:#0b5fa5;
    --deep:#0b4f95;
    --sky:#00a3e4;
    --ink:#1d2a8a;
    --paper:#ffffff;
    --stage:#e6e6e6;
    --text:#333;
  }
  *{box-sizing:border-box;margin:0;padding:0}
  html,body{width:1200px;height:900px;overflow:hidden;background:var(--stage)}
  .flyer{position:absolute;left:283px;top:10px;width:634px;height:880px;background:var(--paper);overflow:hidden;font-family:"Open Sans",sans-serif}
  .flyer-shapes{position:absolute;inset:0}
  .forum-label{position:absolute;left:11px;top:8px;color:#fff;font-family:"Roboto",sans-serif;font-weight:500;font-size:21px}
  .forum-title{position:absolute;left:11px;top:96px;color:#fff;font-family:"Roboto Condensed",sans-serif;font-weight:700;font-size:37px;line-height:49px;letter-spacing:-.3px}
  .brand{position:absolute;left:357px;top:14px;display:flex;align-items:center;gap:10px}
  .brand-dot{width:46px;height:46px;border-radius:50%;background:var(--blue)}
  .brand-name{font-family:"Roboto",sans-serif;font-weight:500;font-size:24px;color:var(--navy);line-height:1}
  .brand-sub{font-family:"Roboto",sans-serif;font-weight:500;font-size:6px;color:var(--navy);margin-top:5px}
  .topics{position:absolute;left:2px;top:268px;list-style:none}
  .topics li{display:flex;align-items:center;gap:16px;height:29px;font-family:"Roboto",sans-serif;font-weight:500;font-size:16px;color:var(--ink)}
  .topics svg{width:22px;height:14px;flex:none}
  .city-photo{position:absolute;left:100px;top:366px;width:534px;height:286px;border-radius:143px 0 0 143px;background:linear-gradient(180deg,#c3cccc 0%,#93a08c 40%,#5d6b5a 100%);border:4px solid var(--sky);border-right:0}
  .event-info{position:absolute;left:28px;top:684px;width:580px;display:flex;justify-content:space-between}
  .event-col{width:260px;font-size:8px;line-height:12px;color:var(--text)}
  .event-col p{margin-bottom:10px}
  .event-col b{font-weight:700;color:#111}
  .save-date{font-size:9px;line-height:13px;color:var(--ink)}
  .contact{position:absolute;left:387px;top:834px;color:#fff;font-size:12px;line-height:16px}
</style>
</head>
<body>
<main class="flyer">
  <svg class="flyer-shapes" viewBox="0 0 634 880" aria-hidden="true">
    <defs>
      <linearGradient id="headerBlue" x1="0" y1="0" x2="1" y2="0.3">
        <stop offset="0" stop-color="#1b2f6e"/>
        <stop offset="0.6" stop-color="#0b5fa5"/>
        <stop offset="1" stop-color="#00a3e4"/>
      </linearGradient>
      <linearGradient id="pillBlue" x1="0" y1="1" x2="1" y2="0">
        <stop offset="0" stop-color="#0b4f95"/>
        <stop offset="1" stop-color="#00a3e4"/>
      </linearGradient>
      <linearGradient id="footBlue" x1="0" y1="0" x2="1" y2="0">
        <stop offset="0" stop-color="#00a3e4"/>
        <stop offset="1" stop-color="#0b4f95"/>
      </linearGradient>
    </defs>
    <polygon points="634,170 634,300 100,800 0,880 0,790" fill="#f3f3f5"/>
    <path d="M70 768 L0 840 L0 890 L82 800 Z" fill="#d9d9dc"/>
    <circle cx="74" cy="772" r="13" fill="#d2d2d5"/>
    <path d="M0 0 H290 C300 80 370 118 460 112 L440 135 Q400 212 330 216 H0 Z" fill="url(#headerBlue)"/>
    <path d="M0 219 H330 Q405 214 448 150" fill="none" stroke="#c9c9cc" stroke-width="4"/>
    <ellipse cx="450" cy="0" rx="158" ry="108" fill="#fff"/>
    <path d="M292 0 A158 112 0 0 0 608 0" fill="none" stroke="#c4c4c7" stroke-width="6"/>
    <path d="M300 0 A150 104 0 0 0 600 0" fill="none" stroke="#00a3e4" stroke-width="4"/>
    <path d="M96 246 H320 Q425 240 455 170" fill="none" stroke="url(#footBlue)" stroke-width="4"/>
    <line x1="475" y1="188" x2="660" y2="45" stroke="url(#pillBlue)" stroke-width="30" stroke-linecap="round"/>
    <line x1="550" y1="205" x2="660" y2="125" stroke="url(#pillBlue)" stroke-width="22" stroke-linecap="round"/>
    <line x1="540" y1="248" x2="660" y2="160" stroke="url(#pillBlue)" stroke-width="22" stroke-linecap="round"/>
    <line x1="507" y1="130" x2="592" y2="64" stroke="#111" stroke-width="3"/>
    <line x1="439" y1="262" x2="522" y2="193" stroke="#00a3e4" stroke-width="3"/>
    <line x1="418" y1="317" x2="502" y2="249" stroke="#111" stroke-width="3"/>
    <path d="M243 361 H634" stroke="#0b4f95" stroke-width="3"/>
    <path d="M243 657 H634" stroke="#c4c4c7" stroke-width="3"/>
    <path d="M280 880 Q330 830 380 824 H634 V880 Z" fill="url(#footBlue)"/>
  </svg>

  <div class="forum-label">2019 Vemtora Forum</div>
  <h1 class="forum-title">The Three-Legged Stool<br>Balanced or Broken?</h1>

  <div class="brand">
    <span class="brand-dot"></span>
    <div>
      <div class="brand-name">I-Vemtora</div>
      <div class="brand-sub">Institute for Building Project Leadership</div>
    </div>
  </div>

  <ul class="topics">
    <li><svg viewBox="0 0 22 14"><path d="M1 4 L6 2 L11 5 L16 2 L21 4 V9 L16 12 L11 9 L6 12 L1 9 Z" fill="none" stroke="#444" stroke-width="1.3"/></svg>The Right Contract management</li>
    <li><svg viewBox="0 0 22 14"><path d="M1 4 L6 2 L11 5 L16 2 L21 4 V9 L16 12 L11 9 L6 12 L1 9 Z" fill="none" stroke="#444" stroke-width="1.3"/></svg>The Right Culture</li>
    <li><svg viewBox="0 0 22 14"><path d="M1 4 L6 2 L11 5 L16 2 L21 4 V9 L16 12 L11 9 L6 12 L1 9 Z" fill="none" stroke="#444" stroke-width="1.3"/></svg>The Right Subcontractors</li>
  </ul>

  <div class="city-photo" role="img" aria-label="Aerial photo of a riverside city skyline with glass office towers"></div>

  <section class="event-info">
    <div class="event-col">
      <p class="save-date"><b>Save the Date: October 17 – 18, 2019</b></p>
      <p><b>Thursday : Opening Keynote</b> – Panel: Owner, Contractor and Designer</p>
      <p><b>Lunch Presentation</b></p>
    </div>
    <div class="event-col">
      <p class="save-date"><b>Bel Costano Resort and Spa, Houston, Texas</b></p>
      <p><b>Friday : Closing Keynote, Dale Hutton</b></p>
      <p><b>Final Wrap-Up</b> – Door Prizes</p>
    </div>
  </section>

  <div class="contact">Contact Us : Office: (512) 555-0147<br>www.i-vemtora.com</div>
</main>
</body>
</html>
```